Take my logo and make me some cool looking business cards

I've got a logo that we've trademarked so you can't change the logo but you can change it's color combo and find a fun way to incorporate it into a new business card design that is fresh, stylish, and can be applied to some cool medium cost materials (plastic, wood, metal, etc). Basically, we're looking for business cards that stand out in a good way.
Updates
Here's the logo we're currently using:
Thanks to everyone that has submitted designs. We've narrowed down to the top 4 designs and tried to eliminate old versions or designs that just didn't match our vision as quickly as we could. We don't plan on keeping this open for the full 9 days; we plan on selecting a design in the next 48 hours; with the goal of having something in the hands of a printer, preferably plastic printer, by Thursday AM Pacific Time.
Industry/Entity Type
Business
Requirements
Must have
- must include our existing logo

```html
<!DOCTYPE html>
<html lang="en">
<head>
<meta charset="utf-8">
<title>Halden Business Cards</title>
<link href="https://fonts.googleapis.com/css2?family=Lato:wght@400;700&display=swap" rel="stylesheet">
<style>
  :root {
    --backdrop: #1e1e1e;
    --card: #ffffff;
    --brand-red: #cc0000;
    --band-grey: #454545;
    --ink: #3a3a3a;
  }
  * { margin: 0; padding: 0; box-sizing: border-box; }
  html, body { width: 1200px; height: 900px; overflow: hidden; }
  body {
    background: var(--backdrop);
    font-family: "Lato", sans-serif;
    color: var(--ink);
    position: relative;
  }
  .card {
    position: absolute;
    top: 300px;
    width: 520px;
    height: 300px;
    background: var(--card);
    overflow: hidden;
  }
  .card--front { left: 50px; }
  .card--back { left: 630px; }
  .card__band {
    position: absolute;
    left: 0;
    width: 520px;
    height: 36px;
  }
  .card__band--top { top: 0; }
  .card__band--bottom { bottom: 0; }
  .company-name {
    position: absolute;
    font-family: "Lato", sans-serif;
    font-weight: 700;
    color: var(--ink);
    letter-spacing: 4px;
    white-space: nowrap;
  }
  .card--front .company-name {
    left: 0; right: 0; top: 120px;
    text-align: center;
    font-size: 48px;
    line-height: 60px;
  }
  .card--back .company-name {
    left: 250px; top: 56px;
    font-size: 32px;
    line-height: 40px;
  }
  .holder {
    position: absolute;
    left: 40px; top: 110px;
    font-size: 15px;
    line-height: 1.15;
    text-transform: uppercase;
  }
  .holder__name { font-weight: 700; }
  .contacts {
    position: absolute;
    left: 280px; top: 128px;
    list-style: none;
    font-size: 14px;
  }
  .contacts__item {
    display: flex;
    align-items: flex-start;
    gap: 8px;
    margin-bottom: 12px;
    line-height: 1.2;
  }
  .contacts__icon {
    flex: none;
    width: 20px; height: 20px;
  }
</style>
</head>
<body>

<section class="card card--front">
  <svg class="card__band card__band--top" viewBox="0 0 520 36">
    <rect width="520" height="18" fill="var(--brand-red)"/>
    <polygon points="0,18 520,18 505,34 15,34" fill="var(--band-grey)"/>
  </svg>
  <p class="company-name">HALDEN</p>
  <svg class="card__band card__band--bottom" viewBox="0 0 520 36">
    <polygon points="15,2 505,2 520,18 0,18" fill="var(--band-grey)"/>
    <rect y="18" width="520" height="18" fill="var(--brand-red)"/>
  </svg>
</section>

<section class="card card--back">
  <svg class="card__band card__band--top" viewBox="0 0 520 36">
    <rect width="520" height="18" fill="var(--brand-red)"/>
    <polygon points="0,18 520,18 505,34 15,34" fill="var(--band-grey)"/>
  </svg>
  <p class="company-name">HALDEN</p>
  <div class="holder">
    <p class="holder__name">Jordan Hale</p>
    <p class="holder__title">CEO</p>
  </div>
  <ul class="contacts">
    <li class="contacts__item">
      <svg class="contacts__icon" viewBox="0 0 20 20"><rect width="20" height="20" rx="3" fill="var(--brand-red)"/><path d="M4 8c0-2 3-3 6-3s6 1 6 3l-2 1-1-2H7L6 9z M6 10h8l1 5H5z" fill="#fff"/></svg>
      <span>+14085550142</span>
    </li>
    <li class="contacts__item">
      <svg class="contacts__icon" viewBox="0 0 20 20"><rect width="20" height="20" rx="3" fill="var(--brand-red)"/><rect x="4" y="6" width="12" height="8" fill="#fff"/><path d="M4 6l6 5 6-5" fill="none" stroke="var(--brand-red)" stroke-width="1.2"/></svg>
      <span>jh@halden.com</span>
    </li>
    <li class="contacts__item">
      <svg class="contacts__icon" viewBox="0 0 20 20"><rect width="20" height="20" rx="3" fill="var(--brand-red)"/><path d="M10 4l6 6h-2v6H6v-6H4z" fill="#fff"/></svg>
      <span>412 Marlow Avenue<br>Pine Harbor,<br>CA 94000</span>
    </li>
  </ul>
  <svg class="card__band card__band--bottom" viewBox="0 0 520 36">
    <polygon points="15,2 505,2 520,18 0,18" fill="var(--band-grey)"/>
    <rect y="18" width="520" height="18" fill="var(--brand-red)"/>
  </svg>
</section>

</body>
</html>
```